Beautiful design for wordpress

I need a beautiful, colourful and feminine website. My business is called 'The Moonlit Brook', and I sell crystals, books, CD's, pendulums and other metaphysical items. I also provide Reiki (energy healing).
I want this design to be eye catching and inspire happiness and joy in those who see it. And I would love to see the use of the logo and its colours :)
Please add these on the web design: Home, About, Online store, Blog

• Colourful and playful, must use the logo somewhere, have the words on a menu saying 'Home, Blog, Online store and about' (or similar to those)And the design must stand out!
• grey, brown and other boring colours.

```html
<!DOCTYPE html>
<html lang="en">
<head>
<meta charset="utf-8">
<title>The Moonlit Brook — Crystals &amp; Gifts</title>
<link href="https://fonts.googleapis.com/css2?family=Oswald:wght@300;400;500&family=Roboto+Condensed:wght@400;700&display=swap" rel="stylesheet">
<style>
  :root {
    --red: #e8575a;
    --red-soft: rgba(232, 87, 90, 0.85);
    --ink: #222222;
    --text: #555555;
    --muted: #888888;
    --line: #dddddd;
    --band: #262626;
    --band-title: #8a8a8a;
    --band-text: #7a7a7a;
    --white: #ffffff;
  }
  * { margin: 0; padding: 0; box-sizing: border-box; }
  html, body { width: 752px; height: 1200px; overflow: hidden; background: var(--white); }
  body { position: relative; font-family: "Roboto Condensed", "Arial Narrow", sans-serif; color: var(--text); }
  .abs { position: absolute; }

  /* Header */
  .brand { left: 108px; top: 22px; width: 100px; }
  .brand-mark { width: 12px; height: 12px; border-radius: 50%; background: var(--red); margin-bottom: 4px; }
  .brand-name { font-family: "Oswald", sans-serif; font-weight: 400; font-size: 17px; line-height: 19px; color: #6b6b6b; }
  .brand-tag { font-family: "Oswald", sans-serif; font-size: 5px; letter-spacing: 1px; color: #6b6b6b; margin-top: 6px; }

  .util-nav { right: 108px; top: 30px; display: flex; gap: 0; font-size: 6px; color: #444; text-transform: uppercase; }
  .util-nav span { padding: 0 12px; }
  .util-nav span:last-child { padding-right: 0; }
  .util-nav .sep { padding: 0; }

  .search { left: 402px; top: 52px; width: 144px; height: 15px; border: 1px solid #ccc; display: flex; }
  .search-input { flex: 1; font-size: 5px; color: #999; padding: 4px 6px; text-transform: uppercase; }
  .search-btn { width: 35px; background: var(--red); color: var(--white); font-size: 5px; text-align: center; line-height: 13px; text-transform: uppercase; }

  .cart { left: 558px; top: 52px; width: 86px; height: 15px; border: 1px solid #ccc; font-size: 5px; color: #444; display: flex; align-items: center; gap: 5px; padding-left: 8px; text-transform: uppercase; }
  .cart b { color: var(--red); font-weight: 400; }

  .main-nav { right: 108px; top: 82px; display: flex; gap: 34px; font-family: "Oswald", sans-serif; font-size: 9px; color: #333; text-transform: uppercase; }

  /* Hero */
  .hero { left: 89px; top: 106px; width: 556px; height: 259px; background: linear-gradient(100deg, #4a4a4a 0%, #7a6a60 30%, #5e5a58 55%, #4c4c4c 100%); }
  .offer { left: 456px; top: 124px; width: 100px; height: 100px; border-radius: 50%; background: var(--red); color: var(--white); text-align: center; font-family: "Oswald", sans-serif; }
  .offer .pct { font-size: 30px; line-height: 30px; margin-top: 20px; }
  .offer .word { font-size: 13px; line-height: 14px; }
  .offer .note { font-size: 7px; margin-top: 3px; }
  .hero-title { left: 414px; top: 232px; font-family: "Oswald", sans-serif; font-weight: 400; font-size: 28px; color: var(--white); white-space: nowrap; }
  .hero-text { left: 418px; top: 275px; width: 210px; font-family: "Oswald", sans-serif; font-weight: 300; font-size: 9.5px; line-height: 15px; color: var(--white); text-transform: uppercase; }
  .hero-arrows { left: 601px; top: 339px; display: flex; gap: 1px; }
  .hero-arrows span { width: 17px; height: 17px; background: var(--red); display: flex; align-items: center; justify-content: center; }

  /* Welcome */
  .section-title { left: 0; width: 752px; text-align: center; font-family: "Oswald", sans-serif; font-weight: 400; color: var(--ink); text-transform: uppercase; }
  .welcome-title { top: 382px; font-size: 19px; }
  .blurb { left: 136px; width: 480px; text-align: center; font-size: 5.8px; line-height: 12.5px; color: var(--text); text-transform: uppercase; }
  .welcome-text { top: 414px; }

  /* Category tiles */
  .tile { top: 471px; width: 169px; height: 169px; }
  .tile-band { position: absolute; left: 0; top: 114px; width: 100%; height: 47px; background: var(--red-soft); color: var(--white); padding: 5px 12px; }
  .tile-band h3 { font-family: "Oswald", sans-serif; font-weight: 400; font-size: 17px; line-height: 20px; }
  .tile-band p { font-size: 6.5px; text-transform: uppercase; margin-top: 3px; }
  .tile-crystals { left: 107px; background: linear-gradient(135deg, #4a3a35, #8a2f48 60%, #5a4a44); }
  .tile-books { left: 292px; background: linear-gradient(135deg, #6b7a5a, #d8d4cc 45%, #5c4434); }
  .tile-pendulums { left: 475px; background: linear-gradient(135deg, #6a3c34, #c88878 50%, #3a4a6a); }

  /* Products */
  .products-title { top: 665px; font-size: 19px; }
  .product { top: 707px; width: 124px; text-align: center; }
  .product-img { width: 124px; height: 108px; }
  .product-name { font-family: "Oswald", sans-serif; font-size: 10px; color: var(--ink); margin-top: 9px; text-transform: uppercase; }
  .product-price { font-family: "Oswald", sans-serif; font-size: 11px; color: var(--red); margin-top: 3px; }
  .add-to-cart { display: flex; width: 85px; height: 20px; margin: 4px auto 0; background: var(--red); color: var(--white); font-family: "Oswald", sans-serif; font-size: 7px; text-transform: uppercase; }
  .add-to-cart .ico { width: 21px; border-right: 1px solid rgba(255,255,255,0.6); display: flex; align-items: center; justify-content: center; }
  .add-to-cart .lbl { flex: 1; line-height: 20px; }
  .p1 { left: 107px; } .p1 .product-img { background: linear-gradient(135deg, #c9b9a6, #b8703a 50%, #a9b7a0); }
  .p2 { left: 245px; } .p2 .product-img { background: radial-gradient(circle at 50% 45%, #8a8f96 0%, #7a6426 35%, #3a3a3a 75%); }
  .p3 { left: 382px; } .p3 .product-img { background: linear-gradient(90deg, #3a2418, #7a4a2c 30%, #4c2e1e 60%, #8a5a3a); }
  .p4 { left: 520px; } .p4 .product-img { background: radial-gradient(circle at 45% 60%, #d8d8d8 0%, #a0a0a0 40%, #5a5a5a 90%); }

  /* Safe shop band */
  .safe { left: 107px; top: 914px; width: 537px; height: 104px; background: var(--band); }
  .safe h2 { position: absolute; left: 0; width: 100%; top: 14px; text-align: center; font-family: "Oswald", sans-serif; font-weight: 400; font-size: 19px; color: var(--band-title); }
  .safe .blurb { left: 28px; top: 49px; color: var(--band-text); }

  /* Footer */
  .footer-col { top: 1038px; }
  .footer-col h4 { font-family: "Oswald", sans-serif; font-weight: 400; font-size: 8px; color: var(--ink); text-transform: uppercase; margin-bottom: 4px; }
  .footer-col li { list-style: none; font-size: 5.5px; line-height: 13.6px; color: #555; text-transform: uppercase; }
  .c1 { left: 108px; } .c2 { left: 210px; } .c3 { left: 328px; } .c4 { left: 430px; } .c5 { left: 532px; }
  .social { display: flex; gap: 6px; margin-top: 4px; }
  .social span { width: 16px; height: 16px; border-radius: 50%; background: #777; }
  .cards { display: flex; gap: 5px; margin-top: 15px; }
  .cards span { width: 18px; height: 11px; border-radius: 2px; background: #c9c9c9; border: 1px solid #aaa; }

  .footer-rule { left: 107px; top: 1151px; width: 537px; height: 1px; background: var(--line); }
  .copyright { left: 0; top: 1164px; width: 752px; text-align: center; font-size: 5.5px; color: #444; text-transform: uppercase; }
</style>
</head>
<body>

<header>
  <div class="abs brand">
    <div class="brand-mark"></div>
    <div class="brand-name">The Moonlit Brook</div>
    <div class="brand-tag">CRYSTALS &amp; GIFTS</div>
  </div>

  <nav class="abs util-nav">
    <span>Home</span><span class="sep">|</span>
    <span>My Account</span><span class="sep">|</span>
    <span>Login</span><span class="sep">|</span>
    <span>Register</span>
  </nav>

  <div class="abs search">
    <div class="search-input">Search your items :</div>
    <div class="search-btn">Search</div>
  </div>

  <div class="abs cart">
    <svg width="7" height="6" viewBox="0 0 14 12"><path d="M0 1h3l2 7h7l2-5H4" fill="none" stroke="#333" stroke-width="1.6"/><circle cx="6" cy="10.5" r="1.2" fill="#333"/><circle cx="11" cy="10.5" r="1.2" fill="#333"/></svg>
    <span>Your cart is : <b>0 items</b></span>
  </div>

  <nav class="abs main-nav">
    <span>Home</span><span>About</span><span>Online Store</span><span>Blog</span><span>Contact Us</span>
  </nav>
</header>

<section>
  <div class="abs hero" role="img" aria-label="Photo of a woman with dark hair wearing beaded crystal earrings, resting her chin on her hand"></div>
  <div class="abs offer">
    <div class="pct">20%</div>
    <div class="word">OFFER</div>
    <div class="note">FOR APRIL ONLY</div>
  </div>
  <h1 class="abs hero-title">THE MOONLIT BROOK</h1>
  <p class="abs hero-text">I sell crystals, books, CD's, pendulums and other metaphysical items. I also provide Reiki (energy healing).</p>
  <div class="abs hero-arrows">
    <span><svg width="6" height="8" viewBox="0 0 6 8"><path d="M5 0.5L1.5 4 5 7.5" fill="none" stroke="#fff" stroke-width="1.2"/></svg></span>
    <span><svg width="6" height="8" viewBox="0 0 6 8"><path d="M1 0.5L4.5 4 1 7.5" fill="none" stroke="#fff" stroke-width="1.2"/></svg></span>
  </div>
</section>

<section>
  <h2 class="abs section-title welcome-title">Welcome to The Moonlit Brook</h2>
  <p class="abs blurb welcome-text">It is a long established fact that a reader will be distracted by the readable content of a page when looking at its layout. The point of using Lorem Ipsum is that it has a more-or-less normal distribution of letters, as opposed to using 'Content here, content here', making it look like readable English. Many desktop publishing packages and web page editors now use Lorem Ipsum as their default model text...</p>

  <div class="abs tile tile-crystals" role="img" aria-label="Photo of a pink faceted crystal pendant on a silver chain">
    <div class="tile-band"><h3>CRYSTALS</h3><p>Check some of our premium products...</p></div>
  </div>
  <div class="abs tile tile-books" role="img" aria-label="Photo of a woman reading an open book in a hammock">
    <div class="tile-band"><h3>BOOKS</h3><p>Check some of our premium products...</p></div>
  </div>
  <div class="abs tile tile-pendulums" role="img" aria-label="Photo of a hand wearing a blue gemstone ring">
    <div class="tile-band"><h3>PENDULUMS</h3><p>Check some of our premium products...</p></div>
  </div>
</section>

<section>
  <h2 class="abs section-title products-title">Our Products</h2>

  <div class="abs product p1">
    <div class="product-img" role="img" aria-label="Photo of wire-wrapped stone pendants"></div>
    <div class="product-name">Metaphysical</div>
    <div class="product-price">$89.90</div>
    <div class="add-to-cart"><span class="ico"><svg width="9" height="8" viewBox="0 0 14 12"><path d="M0 1h3l2 7h7l2-5H4" fill="none" stroke="#fff" stroke-width="1.5"/><circle cx="6" cy="10.5" r="1.2" fill="#fff"/><circle cx="11" cy="10.5" r="1.2" fill="#fff"/></svg></span><span class="lbl">Add to cart</span></div>
  </div>
  <div class="abs product p2">
    <div class="product-img" role="img" aria-label="Photo of an ornate gold ring with a clear crystal"></div>
    <div class="product-name">Crystals</div>
    <div class="product-price">$89.90</div>
    <div class="add-to-cart"><span class="ico"><svg width="9" height="8" viewBox="0 0 14 12"><path d="M0 1h3l2 7h7l2-5H4" fill="none" stroke="#fff" stroke-width="1.5"/><circle cx="6" cy="10.5" r="1.2" fill="#fff"/><circle cx="11" cy="10.5" r="1.2" fill="#fff"/></svg></span><span class="lbl">Add to cart</span></div>
  </div>
  <div class="abs product p3">
    <div class="product-img" role="img" aria-label="Photo of old leather-bound books on a shelf"></div>
    <div class="product-name">Books</div>
    <div class="product-price">$89.90</div>
    <div class="add-to-cart"><span class="ico"><svg width="9" height="8" viewBox="0 0 14 12"><path d="M0 1h3l2 7h7l2-5H4" fill="none" stroke="#fff" stroke-width="1.5"/><circle cx="6" cy="10.5" r="1.2" fill="#fff"/><circle cx="11" cy="10.5" r="1.2" fill="#fff"/></svg></span><span class="lbl">Add to cart</span></div>
  </div>
  <div class="abs product p4">
    <div class="product-img" role="img" aria-label="Photo of a stack of silver compact discs"></div>
    <div class="product-name">CD's</div>
    <div class="product-price">$89.90</div>
    <div class="add-to-cart"><span class="ico"><svg width="9" height="8" viewBox="0 0 14 12"><path d="M0 1h3l2 7h7l2-5H4" fill="none" stroke="#fff" stroke-width="1.5"/><circle cx="6" cy="10.5" r="1.2" fill="#fff"/><circle cx="11" cy="10.5" r="1.2" fill="#fff"/></svg></span><span class="lbl">Add to cart</span></div>
  </div>
</section>

<section class="abs safe">
  <h2>SAFE SHOP</h2>
  <p class="abs blurb">It is a long established fact that a reader will be distracted by the readable content of a page when looking at its layout. The point of using Lorem Ipsum is that it has a more-or-less normal distribution of letters, as opposed to using 'Content here, content here', making it look like readable English. Many desktop publishing packages and web page editors now use Lorem Ipsum as their default model text...</p>
</section>

<footer>
  <div class="abs footer-col c1">
    <h4>Information</h4>
    <ul><li>About</li><li>Delivery</li><li>Checkout</li><li>Privacy Policy</li><li>My Account</li></ul>
  </div>
  <div class="abs footer-col c2">
    <h4>Categories</h4>
    <ul><li>My Orders</li><li>My Credit Slips</li><li>My Addresses</li><li>My Personal Info</li><li>My Vouchers</li><li>My Loyalty Points</li></ul>
  </div>
  <div class="abs footer-col c3">
    <h4>Extras</h4>
    <ul><li>Brands</li><li>Gift Vouchers</li><li>Affiliates</li><li>Specials</li></ul>
  </div>
  <div class="abs footer-col c4">
    <h4>Shopping Guide</h4>
    <ul><li>How to Buy</li><li>FAQ's</li><li>Payment</li><li>Shipment</li></ul>
  </div>
  <div class="abs footer-col c5">
    <h4>Follow Us :</h4>
    <div class="social"><span></span><span></span><span></span><span></span><span></span></div>
    <div class="cards"><span></span><span></span><span></span><span></span><span></span></div>
  </div>

  <div class="abs footer-rule"></div>
  <p class="abs copyright">Copyright © 2014 The Moonlit Brook. All rights reserved.</p>
</footer>

</body>
</html>
```